What makes us Different Managed Communications Services Provider Flyer

We need a flyer to explain why we are different than other "managed IT services" company. Gives a brief description of our company and services that can entice clients and potential clients to setup a FREE consultation with us. This will become part of an ongoing marketing campaign that includes emails, leave behinds, brochures, and more

```html
<!DOCTYPE html>
<html lang="en">
<head>
<meta charset="utf-8">
<title>Brightpath Voice &amp; Data — More Than Just a Managed IT Provider</title>
<link href="https://fonts.googleapis.com/css2?family=Montserrat:wght@400;500;700;800&family=Michroma&display=swap" rel="stylesheet">
<style>
  :root {
    --navy-deep: #030b1f;
    --navy: #071a3f;
    --royal: #0f4fa8;
    --brand-blue: #1a6fc4;
    --cyan: #16c3e6;
    --cyan-bright: #27d3f2;
    --heading-blue: #1467c0;
    --ink: #3a3f48;
    --ink-strong: #15181d;
    --white: #ffffff;
    --paper: #ffffff;
  }
  * { box-sizing: border-box; margin: 0; padding: 0; }
  html, body { width: 943px; height: 1200px; overflow: hidden; background: #e9ebee; }
  body { font-family: "Montserrat", Arial, sans-serif; }

  .flyer { position: relative; width: 943px; height: 1200px; background: var(--paper); overflow: hidden; }

  /* Hero */
  .hero { position: absolute; left: 0; top: 0; width: 943px; height: 389px; background: var(--navy-deep); overflow: hidden; }
  .hero-photo { position: absolute; inset: 0; background: radial-gradient(ellipse at 68% 45%, #1a7fd0 0%, #0b3470 30%, #05142f 65%, #020816 100%); }
  .hero-shapes { position: absolute; inset: 0; }
  .brand { position: absolute; left: 0; width: 490px; top: 78px; display: flex; justify-content: center; align-items: center; gap: 10px; }
  .brand-dot { width: 18px; height: 18px; border-radius: 50%; background: var(--cyan); }
  .brand-name { font-weight: 700; font-size: 22px; color: var(--white); letter-spacing: .2px; }
  .headline { position: absolute; left: 0; width: 490px; top: 180px; text-align: center; font-weight: 800; line-height: 1; }
  .headline .lead { display: block; color: var(--cyan); font-size: 34px; line-height: 35px; }
  .headline .big { display: block; font-family: "Michroma", sans-serif; color: var(--cyan); font-size: 45px; line-height: 52px; margin-top: 2px; letter-spacing: -1px; }
  .headline .sub { display: block; color: var(--white); font-size: 32px; line-height: 35px; margin-top: 2px; }

  /* Intro band */
  .intro { position: absolute; left: 0; top: 389px; width: 943px; height: 124px; background: linear-gradient(90deg, var(--brand-blue) 0%, #1452a6 55%, #0a2a66 100%); }
  .intro p { position: absolute; left: 83px; top: 18px; width: 680px; color: var(--white); font-size: 11.6px; line-height: 14.9px; }
  .intro strong { font-weight: 700; }

  /* Body columns */
  .col { position: absolute; }
  .col-left { left: 83px; top: 544px; width: 392px; }
  .col-right { left: 514px; top: 544px; width: 345px; }
  .section-title { font-family: "Michroma", sans-serif; color: var(--heading-blue); font-size: 17.5px; line-height: 20px; text-transform: uppercase; letter-spacing: -.3px; margin-bottom: 13px; }
  .copy { color: var(--ink); font-size: 11.6px; line-height: 14.9px; margin-bottom: 14px; }
  .copy strong { color: var(--ink-strong); font-weight: 700; }
  .col-right .section-title.spaced { margin-top: 22px; }

  .offer-box { position: absolute; left: 83px; top: 746px; width: 388px; height: 335px; background: linear-gradient(180deg, var(--navy-deep) 0%, var(--navy) 40%, var(--royal) 100%); padding: 14px 16px 0 16px; color: var(--white); }
  .offer-box .section-title { color: var(--white); margin-bottom: 4px; }
  .offer-box .copy { color: var(--white); margin-bottom: 8px; }
  .offer-label { color: var(--cyan); font-weight: 700; font-size: 11.5px; letter-spacing: 1px; margin-bottom: 10px; }
  .offer-list { list-style: none; }
  .offer-list li { display: flex; align-items: flex-start; gap: 10px; margin-bottom: 13px; font-size: 11.2px; line-height: 14.4px; }
  .offer-list strong { font-weight: 700; }
  .offer-icon { flex: 0 0 25px; height: 25px; border-radius: 50%; background: var(--cyan); display: flex; align-items: center; justify-content: center; margin-top: 2px; }

  /* Footer */
  .footer { position: absolute; left: 0; top: 1118px; width: 943px; height: 82px; background: var(--navy-deep); }
  .footer svg.bands { position: absolute; inset: 0; }
  .phone { position: absolute; left: 80px; top: 23px; display: flex; align-items: center; gap: 8px; color: var(--white); font-family: "Michroma", sans-serif; font-size: 24px; }
  .web { position: absolute; left: 512px; top: 30px; display: flex; align-items: center; gap: 14px; color: var(--white); font-size: 17px; font-weight: 500; letter-spacing: 2px; }
</style>
</head>
<body>
<main class="flyer">
  <header class="hero">
    <div class="hero-photo" role="img" aria-label="Photo of a hand touching a laptop screen showing a glowing security shield over a digital data backdrop"></div>
    <svg class="hero-shapes" width="943" height="389" viewBox="0 0 943 389">
      <defs>
        <linearGradient id="panel" x1="0" y1="0" x2="0" y2="1">
          <stop offset="0" stop-color="#03091c"/>
          <stop offset="1" stop-color="#061a45"/>
        </linearGradient>
      </defs>
      <polygon points="0,0 393,0 608,389 0,389" fill="url(#panel)"/>
      <polygon points="0,0 393,0 400,16 0,16" fill="#1a6fc4"/>
      <polygon points="393,0 410,0 625,389 608,389" fill="#16c3e6"/>
    </svg>
    <div class="brand">
      <span class="brand-dot"></span>
      <span class="brand-name">Brightpath Voice &amp; Data</span>
    </div>
    <h1 class="headline">
      <span class="lead">MORE THAN JUST</span>
      <span class="lead">A MANAGED</span>
      <span class="big">IT PROVIDER</span>
      <span class="sub">OUR LEGACY OF</span>
      <span class="sub">EXCELLENCE</span>
    </h1>
  </header>

  <section class="intro">
    <p>At our company, we are far more than your typical managed IT provider. Since our founding in <strong>1983</strong>, we have built a reputation based on trust, reliability, and unparalleled service. With <strong>client relationships spanning 20 to 30 years,</strong> we have demonstrated a level of commitment that few IT firms can match. What sets us apart is not just our technical expertise but the <strong>deep, long-term partnerships</strong> we cultivate with our clients—many of whom have stayed <strong>with us without ever being locked into a contract.</strong> That is a testament to the exceptional quality of our service and the trust we have earned over decades.</p>
  </section>

  <section class="col col-left">
    <h2 class="section-title">A Commitment Beyond Contracts</h2>
    <p class="copy">Unlike many managed IT providers who rely on rigid contracts to retain clients, we believe that service excellence speaks for itself. The longevity of our client relationships is rooted in our ability to <strong>anticipate needs, resolve challenges before they escalate, and proactively enhance network &amp; communication infrastructures. Our comprehensive checklists, questionnaires, policies, and procedures, attention to details ensure that every client receives a tailored, best-in-class experience from day one.</strong></p>
  </section>

  <section class="offer-box">
    <h2 class="section-title">A Holistic Approach to IT Management</h2>
    <p class="copy">We don’t just manage IT—we integrate ourselves into your business, ensuring that technology aligns with your strategic goals. Our services go beyond traditional break-fix support;</p>
    <p class="offer-label">WE OFFER:</p>
    <ul class="offer-list">
      <li><span class="offer-icon"><svg width="13" height="13" viewBox="0 0 13 13"><rect x="1" y="2" width="11" height="7" fill="none" stroke="#071a3f" stroke-width="1.4"/><path d="M6.5 9v3M4 12h5" stroke="#071a3f" stroke-width="1.4"/></svg></span><span><strong>Strategic IT Roadmaps</strong><br>customized to drive business growth.</span></li>
      <li><span class="offer-icon"><svg width="13" height="13" viewBox="0 0 13 13"><path d="M6.5 1l5 2v4c0 3-2.5 4.5-5 5.5C4 11.5 1.5 10 1.5 7V3z" fill="none" stroke="#071a3f" stroke-width="1.4"/></svg></span><span><strong>Proactive cybersecurity assessments that</strong><br>help keep businesses secure.</span></li>
      <li><span class="offer-icon"><svg width="13" height="13" viewBox="0 0 13 13"><ellipse cx="6.5" cy="3" rx="5" ry="2" fill="none" stroke="#071a3f" stroke-width="1.4"/><path d="M1.5 3v7c0 1.1 2.2 2 5 2s5-.9 5-2V3" fill="none" stroke="#071a3f" stroke-width="1.4"/></svg></span><span><strong>Comprehensive backup and disaster recovery solutions</strong> that provide peace of mind.</span></li>
      <li><span class="offer-icon"><svg width="13" height="13" viewBox="0 0 13 13"><path d="M2 7l3 3 6-7" fill="none" stroke="#071a3f" stroke-width="1.8"/></svg></span><span><strong>Industry-leading response times and dedicated support teams</strong> focused on delivering an exceptional client experience.</span></li>
    </ul>
  </section>

  <section class="col col-right">
    <h2 class="section-title">Our Clients Stay Because We Deliver</h2>
    <p class="copy">For over 40 years, we have maintained a standard of excellence that <strong>other companies simply cannot compare with.</strong> Our team of experts consistently goes above and beyond, ensuring that clients not only <strong>get the support they need but also receive the strategic guidance necessary to stay ahead in an ever-evolving digital landscape.</strong></p>
    <p class="copy">Our <strong>90-day performance review</strong> process ensures that we continuously improve our service based on client feedback. This process allows us to <strong>adapt, refine, and enhance our approach,</strong> providing a truly personalized IT experience that aligns with business objectives.</p>
    <h2 class="section-title spaced">A Legacy of Trust &amp; Reliability</h2>
    <p class="copy">The fact that many of our clients have remained with us for <strong>decades without a formal contract</strong> speaks volumes about the trust we have built. We don’t lock in clients with paperwork—we keep them with results. <strong>That’s the difference between a standard managed IT provider and an IT partner who genuinely cares.</strong></p>
    <p class="copy">If you’re looking for an IT provider that will treat your business as if it were their own, look no further.</p>
    <p class="copy">Our legacy of service, innovation, and commitment to our clients is what sets us apart from the rest.</p>
  </section>

  <footer class="footer">
    <svg class="bands" width="943" height="82" viewBox="0 0 943 82">
      <polygon points="0,0 424,0 470,82 0,82" fill="#1a6fc4"/>
      <polygon points="424,0 440,0 486,82 470,82" fill="#16c3e6"/>
    </svg>
    <div class="phone">
      <svg width="22" height="22" viewBox="0 0 24 24"><path d="M6.6 10.8a15 15 0 0 0 6.6 6.6l2.2-2.2c.3-.3.7-.4 1-.2 1.1.4 2.3.6 3.6.6.6 0 1 .4 1 1V20c0 .6-.4 1-1 1A17 17 0 0 1 3 4c0-.6.4-1 1-1h3.5c.6 0 1 .4 1 1 0 1.3.2 2.5.6 3.6.1.3 0 .7-.2 1z" fill="none" stroke="#fff" stroke-width="2"/></svg>
      <span>713-555-0148</span>
    </div>
    <div class="web">
      <svg width="22" height="22" viewBox="0 0 24 24"><circle cx="12" cy="12" r="10" fill="none" stroke="#16c3e6" stroke-width="2"/><path d="M2 12h20M12 2c3 3 3 17 0 20M12 2c-3 3-3 17 0 20" fill="none" stroke="#16c3e6" stroke-width="1.6"/></svg>
      <span>www.brightpathvd.com</span>
    </div>
  </footer>
</main>
</body>
</html>
```